COMMERCIAL DOOR REPAIR
BUSINESS CARDS, LETTERHEAD, ENVELOPES, FAX COVER, EMAIL SIGNATURE
Rob Whitfield
NFPEI Certified Door Inspector
1752 E Pinnell Ln Glendale, AZ 85317
service@robsgatefix.com
www.robsgatefix.com
ROC# 514037
Not sure if font in logo can be used - open to other fonts as well. just no script or femine fonts. Not sure if all items on back will fit - open to re-wording, suggestions, etc.
24 Hour Emergency Services Available Specializing in: Automatic Doors Manual Doors Vitrelon Glass Doors Hollow Metal Doors Revolving Doors Also specializing in: Glass Mirrors Locksmithing Shower Doors Roof Hatches Re-seals Board-Ups

```html
<!DOCTYPE html>
<html lang="en">
<head>
<meta charset="utf-8">
<title>Harrow Door Works – Stationery Set</title>
<link rel="stylesheet" href="https://fonts.googleapis.com/css2?family=Roboto+Condensed:wght@400;700&family=Open+Sans:wght@400;600;700&display=swap">
<style>
  :root{
    --blue:#1d5aa6;
    --blue-dark:#123f7a;
    --red:#d3262e;
    --paper:#ffffff;
    --ink:#3b3f45;
    --rule:#b9c3cf;
    --tint:#e6eef8;
    --stage:#e9e9e7;
  }
  *{box-sizing:border-box;margin:0;padding:0}
  html,body{width:1200px;height:538px;overflow:hidden;background:var(--stage)}
  body{position:relative;font-family:"Open Sans",Arial,sans-serif;color:var(--ink)}
  .piece{position:absolute;background:var(--paper);box-shadow:0 2px 6px rgba(0,0,0,.18);overflow:hidden}
  .brand{display:flex;align-items:center;gap:3px}
  .brand-mark{width:10px;height:10px;background:var(--red);flex:none}
  .brand-name{font-family:"Roboto Condensed",Arial,sans-serif;font-weight:700;color:var(--blue);font-size:9px;letter-spacing:.2px;white-space:nowrap}
  .brand-tag{font-size:3.6px;color:var(--red);font-weight:700;letter-spacing:.4px;margin-top:1px;white-space:nowrap}
  .tiny{font-size:3.6px;line-height:1.45;white-space:nowrap}
  .stripe{position:absolute;left:0;right:0;height:3px;bottom:0;background:var(--blue)}
  .stripe.red{height:2px;bottom:3px;background:var(--red)}
  .footer{position:absolute;left:0;right:0;bottom:9px;text-align:center;font-size:3.6px;white-space:nowrap}
  .masthead{position:absolute;left:14px;top:14px}
  .masthead .tiny{margin-top:2px}

  /* envelope front */
  .envelope-front{left:29px;top:36px;width:264px;height:132px}
  .envelope-front .masthead{left:12px;top:12px}

  /* envelope back */
  .envelope-back{left:312px;top:36px;width:264px;height:132px}
  .envelope-back svg{position:absolute;left:0;top:0}

  /* business cards */
  .card-front{left:600px;top:43px;width:204px;height:101px}
  .card-front .masthead{left:10px;top:10px}
  .card-front .person{position:absolute;left:10px;top:42px}
  .card-front .person b{display:block;font-size:5.6px;color:var(--blue)}
  .card-front .contact{position:absolute;left:10px;top:62px}
  .card-back{left:804px;top:43px;width:204px;height:101px;background:var(--blue);color:#fff}
  .card-back h2{position:absolute;left:10px;top:8px;font-family:"Roboto Condensed",Arial,sans-serif;font-size:7px;white-space:nowrap}
  .card-back .lede{position:absolute;left:10px;top:20px;font-size:4.2px;font-weight:600}
  .card-back ul{list-style:none;position:absolute;top:29px;font-size:4px;line-height:1.5;white-space:nowrap}
  .card-back .col-a{left:10px}
  .card-back .col-b{left:106px}
  .card-back .lic{position:absolute;left:10px;bottom:7px;font-size:3.8px;white-space:nowrap}
  .card-back .stripe{background:var(--red);height:3px;bottom:0}

  /* full pages */
  .page{top:175px;width:264px;height:330px}
  .letterhead{left:29px}
  .fax{left:312px}
  .invoice{left:600px}
  .quote{left:883px}
  .doc-title{position:absolute;top:50px;left:14px;right:14px;text-align:center;font-family:"Roboto Condensed",Arial,sans-serif;font-weight:700;font-size:6px;color:var(--blue);letter-spacing:.5px}
  .doc-title.right{text-align:right}

  .fax-fields{position:absolute;left:14px;right:14px;top:62px}
  .field{display:flex;align-items:flex-end;gap:4px;font-size:4px;margin-bottom:5px;white-space:nowrap}
  .field span{flex:1;border-bottom:.6px solid var(--rule);height:5px}
  .fax-checks{position:absolute;left:14px;right:14px;top:132px;display:flex;justify-content:space-between;font-size:3.8px}
  .fax-checks i{display:inline-block;width:4px;height:4px;border:.6px solid var(--ink);margin-right:2px;vertical-align:-1px}

  .meta{position:absolute;left:14px;right:14px;top:64px;display:grid;grid-template-columns:1fr 1fr;column-gap:14px}
  .meta .field{margin-bottom:4px}
  .ledger{position:absolute;left:14px;top:100px;border-collapse:collapse;font-size:3.6px;width:calc(100% - 28px)}
  .ledger th{background:var(--blue);color:#fff;font-weight:600;padding:2px;border:.5px solid var(--blue)}
  .ledger td{height:7px;border-left:.5px solid var(--rule);border-right:.5px solid var(--rule);border-bottom:.5px solid var(--tint)}
  .ledger tr:nth-child(even) td{background:var(--tint)}
  .totals{position:absolute;right:14px;top:222px;width:66px;font-size:3.6px}
  .totals div{display:flex;justify-content:space-between;border:.5px solid var(--rule);padding:1px 2px}
  .sign{position:absolute;left:14px;top:268px;width:100px;font-size:3.6px;border-top:.5px solid var(--rule);padding-top:1px}
</style>
</head>
<body>

<section class="piece envelope-front">
  <div class="masthead">
    <div class="brand"><span class="brand-mark"></span><span class="brand-name">HARROW DOOR WORKS</span></div>
    <div class="brand-tag">COMMERCIAL DOOR REPAIR</div>
    <p class="tiny">2286 N Calloway Ave, Glendale, AZ 85319</p>
  </div>
  <div class="stripe red"></div><div class="stripe"></div>
</section>

<section class="piece envelope-back">
  <svg width="264" height="132" viewBox="0 0 264 132">
    <path d="M0 0 H264 V16 L132 52 L0 16 Z" fill="var(--blue)"/>
    <path d="M0 16 L132 52 L264 16" fill="none" stroke="var(--red)" stroke-width="2"/>
    <rect x="126" y="26" width="12" height="12" fill="var(--red)"/>
  </svg>
</section>

<section class="piece card-front">
  <div class="masthead">
    <div class="brand"><span class="brand-mark"></span><span class="brand-name">HARROW DOOR WORKS</span></div>
    <div class="brand-tag">COMMERCIAL DOOR REPAIR</div>
  </div>
  <div class="person">
    <b>Glen Harrow</b>
    <p class="tiny">NFPEI Certified Door Inspector</p>
  </div>
  <div class="contact tiny">
    <p>P (623) 555-0148 &nbsp; F (623) 555-0149</p>
    <p>service@harrowdoorworks.com</p>
    <p>www.harrowdoorworks.com</p>
  </div>
  <div class="stripe red"></div><div class="stripe"></div>
</section>

<section class="piece card-back">
  <h2>24 Hour Emergency Services Available</h2>
  <p class="lede">Specializing in:</p>
  <ul class="col-a">
    <li>Automatic Doors</li><li>Manual Doors</li><li>Vitrelon Glass Doors</li><li>Hollow Metal Doors</li><li>Revolving Doors</li>
  </ul>
  <ul class="col-b">
    <li><b>Also specializing in:</b></li><li>Glass Mirrors · Locksmithing</li><li>Shower Doors · Roof Hatches</li><li>Re-seals · Board-Ups</li>
  </ul>
  <p class="lic">ROC# 730462 · 2286 N Calloway Ave, Glendale, AZ 85319</p>
  <div class="stripe"></div>
</section>

<section class="piece page letterhead">
  <div class="masthead">
    <div class="brand"><span class="brand-mark"></span><span class="brand-name">HARROW DOOR WORKS</span></div>
    <div class="brand-tag">COMMERCIAL DOOR REPAIR</div>
    <p class="tiny">2286 N Calloway Ave, Glendale, AZ 85319</p>
  </div>
  <div class="footer">P (623) 555-0148 · F (623) 555-0149 · service@harrowdoorworks.com · www.harrowdoorworks.com</div>
  <div class="stripe red"></div><div class="stripe"></div>
</section>

<section class="piece page fax">
  <div class="masthead">
    <div class="brand"><span class="brand-mark"></span><span class="brand-name">HARROW DOOR WORKS</span></div>
    <div class="brand-tag">COMMERCIAL DOOR REPAIR</div>
  </div>
  <div class="doc-title">FAX</div>
  <div class="fax-fields">
    <div class="field">To:<span></span>From:<span></span></div>
    <div class="field">Fax:<span></span>Pages:<span></span></div>
    <div class="field">Phone:<span></span>Date:<span></span></div>
    <div class="field">Re:<span></span>CC:<span></span></div>
  </div>
  <div class="fax-checks">
    <span><i></i>Urgent</span><span><i></i>For Review</span><span><i></i>Please Comment</span><span><i></i>Please Reply</span>
  </div>
  <div class="footer">2286 N Calloway Ave, Glendale, AZ 85319 · P (623) 555-0148</div>
  <div class="stripe red"></div><div class="stripe"></div>
</section>

<section class="piece page invoice">
  <div class="masthead">
    <div class="brand"><span class="brand-mark"></span><span class="brand-name">HARROW DOOR WORKS</span></div>
    <p class="tiny">2286 N Calloway Ave, Glendale, AZ 85319 · P (623) 555-0148</p>
  </div>
  <div class="doc-title">INVOICE</div>
  <div class="meta">
    <div class="field">Customer:<span></span></div><div class="field">Date:<span></span></div>
    <div class="field">Address:<span></span></div><div class="field">Invoice #:<span></span></div>
    <div class="field">Phone:<span></span></div><div class="field">Terms:<span></span></div>
  </div>
  <table class="ledger">
    <tr><th style="width:14%">QTY</th><th>DESCRIPTION</th><th style="width:18%">UNIT PRICE</th><th style="width:18%">AMOUNT</th></tr>
    <tr><td></td><td></td><td></td><td></td></tr><tr><td></td><td></td><td></td><td></td></tr>
    <tr><td></td><td></td><td></td><td></td></tr><tr><td></td><td></td><td></td><td></td></tr>
    <tr><td></td><td></td><td></td><td></td></tr><tr><td></td><td></td><td></td><td></td></tr>
    <tr><td></td><td></td><td></td><td></td></tr><tr><td></td><td></td><td></td><td></td></tr>
    <tr><td></td><td></td><td></td><td></td></tr><tr><td></td><td></td><td></td><td></td></tr>
    <tr><td></td><td></td><td></td><td></td></tr><tr><td></td><td></td><td></td><td></td></tr>
    <tr><td></td><td></td><td></td><td></td></tr><tr><td></td><td></td><td></td><td></td></tr>
  </table>
  <div class="totals"><div>Subtotal<span></span></div><div>Tax<span></span></div><div><b>Total</b><span></span></div></div>
  <div class="sign">Signature</div>
  <div class="footer">Thank you for your business · www.harrowdoorworks.com</div>
  <div class="stripe red"></div><div class="stripe"></div>
</section>

<section class="piece page quote">
  <div class="masthead">
    <div class="brand"><span class="brand-mark"></span><span class="brand-name">HARROW DOOR WORKS</span></div>
    <p class="tiny">2286 N Calloway Ave, Glendale, AZ 85319 · P (623) 555-0148</p>
  </div>
  <div class="doc-title right">QUOTE</div>
  <div class="meta">
    <div class="field">Name:<span></span></div><div class="field">Date:<span></span></div>
    <div class="field">Address:<span></span></div><div class="field">Quote #:<span></span></div>
    <div class="field">Phone:<span></span></div><div class="field">Valid:<span></span></div>
  </div>
  <table class="ledger">
    <tr><th style="width:14%">QTY</th><th>DESCRIPTION</th><th style="width:18%">UNIT COST</th><th style="width:18%">TOTAL</th></tr>
    <tr><td></td><td></td><td></td><td></td></tr><tr><td></td><td></td><td></td><td></td></tr>
    <tr><td></td><td></td><td></td><td></td></tr><tr><td></td><td></td><td></td><td></td></tr>
    <tr><td></td><td></td><td></td><td></td></tr><tr><td></td><td></td><td></td><td></td></tr>
    <tr><td></td><td></td><td></td><td></td></tr><tr><td></td><td></td><td></td><td></td></tr>
    <tr><td></td><td></td><td></td><td></td></tr><tr><td></td><td></td><td></td><td></td></tr>
    <tr><td></td><td></td><td></td><td></td></tr><tr><td></td><td></td><td></td><td></td></tr>
    <tr><td></td><td></td><td></td><td></td></tr><tr><td></td><td></td><td></td><td></td></tr>
  </table>
  <div class="totals"><div>Subtotal<span></span></div><div>Tax<span></span></div><div><b>Total</b><span></span></div></div>
  <div class="sign">Approved by</div>
  <div class="footer">Thank you for your business · www.harrowdoorworks.com</div>
  <div class="stripe red"></div><div class="stripe"></div>
</section>

</body>
</html>
```